Beauty Salon Treatment Menu & Pricing

We need a Treatment Pricelist/ Brochure made to hand out to potential & existing customers! Meadowlark Body & Makeup is a small friendly beauty salon focused on the beauty essentials such as waxing, spray tanning, facials & makeup. We have a webpage with our colour theme and style and we would like to brochure to tie in.
www.meadowlarkbodyandmakeup.example.au.
We like a brochure that is clean, simple and easy to read.

Industry/Entity Type

Beauty Salon

```html
<!DOCTYPE html>
<html lang="en">
<head>
<meta charset="utf-8">
<title>Meadowlark Body &amp; Makeup – Treatment Menu</title>
<link rel="stylesheet" href="https://fonts.googleapis.com/css2?family=Arimo:wght@400&display=swap">
<style>
  :root {
    --brand-red: #ed1c2e;
    --ink: #1a1a1a;
    --paper: #ffffff;
  }
  * { margin: 0; padding: 0; box-sizing: border-box; }
  html, body { width: 846px; height: 1200px; overflow: hidden; background: var(--paper); }
  body { font-family: "Arimo", Arial, sans-serif; color: var(--ink); position: relative; }

  .masthead {
    position: absolute; left: 0; top: 0; width: 846px; height: 348px;
    background: var(--brand-red); color: var(--paper); text-align: center;
  }
  .masthead__name {
    position: absolute; left: 0; right: 0; top: 66px;
    font-size: 94px; font-weight: 400; letter-spacing: 0.06em; line-height: 1;
  }
  .masthead__tagline {
    position: absolute; left: 0; right: 0; top: 236px;
    font-size: 48px; font-weight: 400; letter-spacing: 0.14em; line-height: 1;
  }

  .menu-section { position: absolute; }
  .menu-section__title {
    color: var(--brand-red); font-size: 18.5px; font-weight: 400;
    line-height: 22px; margin-bottom: 1px; text-transform: uppercase;
  }
  .price-list {
    display: grid; font-size: 14.5px; line-height: 20px; list-style: none;
  }
  .col-left .price-list { grid-template-columns: 169px auto; }
  .col-right .price-list { grid-template-columns: 225px auto; }
  .price-list__note { grid-column: 1 / -1; }

  .contact {
    position: absolute; left: 425px; top: 1040px;
    font-size: 14.5px; line-height: 20px;
  }
  .contact__label { color: var(--brand-red); font-weight: 400; display: inline-block; width: 19px; }
  .contact__web { color: var(--brand-red); }
</style>
</head>
<body>

<header class="masthead">
  <div class="masthead__name">MEADOWLARK</div>
  <div class="masthead__tagline">BODY &amp; MAKEUP</div>
</header>

<section class="menu-section col-left" style="left:80px; top:401px;">
  <h2 class="menu-section__title">Facial Waxing/ Tint</h2>
  <ul class="price-list">
    <li>Eyebrow</li><li>18.00</li>
    <li>Brow wax &amp; tint</li><li>30.00</li>
    <li>Lip or chin or sides</li><li>10.00</li>
    <li>Brow, lip &amp; chin</li><li>33.00</li>
    <li>Full Face</li><li>38.00</li>
    <li>Lash tint</li><li>20.00</li>
    <li>Brow tint</li><li>16.00</li>
    <li>Lash &amp; Brow tint</li><li>30.00</li>
  </ul>
</section>

<section class="menu-section col-left" style="left:80px; top:617px;">
  <h2 class="menu-section__title">Female Waxing</h2>
  <ul class="price-list">
    <li>Brazilian</li><li>45.00</li>
    <li>Extended Bik</li><li>30.00</li>
    <li>Basic Bikini</li><li>18.00</li>
    <li>Full leg</li><li>45.00</li>
    <li>Full Leg &amp; Basic Bikini</li><li>50.00</li>
    <li>¾ Leg</li><li>35.00</li>
    <li>¾ Leg &amp; Basic Bikini</li><li>45.00</li>
    <li>Half Leg (inc knees)</li><li>30.00</li>
    <li>Full Arm</li><li>30.00</li>
    <li>Half Arm</li><li>25.00</li>
    <li>Underarm</li><li>18.00</li>
    <li>Stomach</li><li>15.00</li>
    <li>Back</li><li>20.00</li>
    <li>Patches, from</li><li>10.00</li>
  </ul>
</section>

<section class="menu-section col-left" style="left:80px; top:954px;">
  <h2 class="menu-section__title">Mens Waxing</h2>
  <ul class="price-list">
    <li>Neck</li><li>25.00</li>
    <li>Back (includes neck)</li><li>40.00</li>
    <li>Chest</li><li>35.00</li>
    <li>Chest &amp; Stoma</li><li>40.00</li>
    <li>Back, Chest &amp; Stomach</li><li>75.00</li>
    <li>Full Leg</li><li>55.00</li>
    <li>Full Arm</li><li>38.00</li>
    <li>Underarm</li><li>20.00</li>
  </ul>
</section>

<section class="menu-section col-right" style="left:425px; top:398px;">
  <h2 class="menu-section__title">Tanning</h2>
  <ul class="price-list">
    <li>Spray Tan (every 10th tan free)</li><li>35.00</li>
    <li>Half Body Spray Tan</li><li>25.00</li>
  </ul>
</section>

<section class="menu-section col-right" style="left:425px; top:493px;">
  <h2 class="menu-section__title">Nails</h2>
  <ul class="price-list">
    <li>Manicure</li><li>40.00</li>
    <li>Gel Colour Gloss Manicure</li><li>50.00</li>
    <li>Mini Manicure (file &amp; polish)</li><li>30.00</li>
    <li>Gel Polish Removal</li><li>15.00</li>
  </ul>
</section>

<section class="menu-section col-right" style="left:425px; top:628px;">
  <h2 class="menu-section__title">Makeup</h2>
  <ul class="price-list">
    <li>Bridal</li><li>95.00</li>
    <li class="price-list__note">(we come to you, min 3 faces. includes lashes)</li>
    <li>Bridal Trial</li><li>100.00</li>
    <li class="price-list__note">includes take home lip colour)</li>
  </ul>
</section>

<section class="menu-section col-right" style="left:425px; top:764px;">
  <h2 class="menu-section__title">Special Occasion</h2>
  <ul class="price-list">
    <li>School Ball</li><li>65.00</li>
    <li>False Lash Application</li><li>25.00</li>
    <li class="price-list__note">(Includes lashes)</li>
  </ul>
</section>

<address class="contact" style="font-style:normal;">
  <div>42 Harbour Walk, Linfield, (Inside Seaside Hair)</div>
  <div><span class="contact__label">P:</span>0400 555 218</div>
  <div><span class="contact__label">E:</span>info@meadowlarkbodyandmakeup.example.au</div>
  <div><span class="contact__label">f:</span>social.example/meadowlarkbodyandmakeup</div>
  <div class="contact__web">www.meadowlarkbodyandmakeup.example.au</div>
</address>

</body>
</html>
```